plumbers buisness card

A buisness card for a plumbing buisness
needs to have a water theme with navy blue, light blue and white
with an image of either a water drop, pipes, tools or something relating to plumbing and incorperating my buisness name as a logo

"Talcott Plumbing" is the words that need to stand out with "& gasfitting" to be smaller
Updates

spelling error on brief, "maintenance"
and also could you include my email m_talcott@nimbrel.com.au

Industry/Entity Type

Plumbing

Contact Information for Business Card

Talcott Plumbing & Gasfitting

myles talcott
0492315806

specialising in
-new homes
-maitenance
-renovations

license no.
-73846

```html
<!DOCTYPE html>
<html lang="en">
<head>
<meta charset="utf-8">
<title>Talcott Plumbing &amp; Gas fitting – Business Card</title>
<link rel="stylesheet" href="https://fonts.googleapis.com/css2?family=Patua+One&family=Arimo&family=Source+Sans+3:wght@300;400&display=swap">
<style>
  :root {
    --navy: #2b3d59;
    --sky: #2e87c2;
    --white: #ffffff;
    --paper: #ffffff;
  }
  * { margin: 0; padding: 0; box-sizing: border-box; }
  html, body {
    width: 947px; height: 1200px; overflow: hidden; background: var(--paper);
  }
  .canvas { position: relative; width: 947px; height: 1200px; }
  .card-face {
    position: absolute; left: 0; width: 947px;
    background: linear-gradient(90deg, var(--navy) 0%, var(--sky) 100%);
    color: var(--white);
  }
  .card-front { top: 0; height: 532px; }
  .card-back { top: 665px; height: 535px; }

  .brand-dot {
    position: absolute; border-radius: 50%; background: var(--white);
  }
  .card-front .brand-dot { left: 70px; top: 205px; width: 190px; height: 190px; }
  .card-back .brand-dot { left: 54px; top: 67px; width: 72px; height: 72px; }

  .brand-name, .brand-trade {
    position: absolute; white-space: nowrap;
    font-family: "Patua One", serif; font-weight: 400; color: var(--white);
    line-height: 1;
  }
  .card-front .brand-name { left: 287px; top: 198px; font-size: 72px; }
  .card-front .brand-trade { left: 468px; top: 286px; font-size: 40px; }
  .card-back .brand-name { left: 144px; top: 71px; font-size: 32px; }
  .card-back .brand-trade { left: 227px; top: 110px; font-size: 18px; }

  .contact {
    position: absolute; right: 77px; top: 182px; text-align: right;
  }
  .contact-name {
    font-family: "Arimo", sans-serif; font-weight: 400;
    font-size: 58px; line-height: 1; margin-bottom: 14px;
  }
  .contact-line {
    font-family: "Source Sans 3", sans-serif; font-weight: 300;
    font-size: 35px; line-height: 47px;
  }
  .services {
    position: absolute; left: 60px; top: 467px; width: 830px;
    font-family: "Source Sans 3", sans-serif; font-weight: 300;
    font-size: 33px; white-space: nowrap; text-align: center;
  }
</style>
</head>
<body>
<div class="canvas">
  <section class="card-face card-front">
    <div class="brand-dot"></div>
    <div class="brand-name">Talcott Plumbing</div>
    <div class="brand-trade">&amp; Gas fitting</div>
  </section>

  <section class="card-face card-back">
    <div class="brand-dot"></div>
    <div class="brand-name">Talcott Plumbing</div>
    <div class="brand-trade">&amp; Gas fitting</div>

    <div class="contact">
      <div class="contact-name">Myles Talcott</div>
      <div class="contact-line">Mob: 0492315806</div>
      <div class="contact-line">Email: m_talcott@nimbrel.com.au</div>
      <div class="contact-line">Lic.&nbsp; No.: 73846</div>
    </div>

    <div class="services">Specialising in New Homes, Maintenance &amp; Renovations</div>
  </section>
</div>
</body>
</html>
```